Animal Horse & Bedding Company Needs a Website Coded & Designed

We need a website for a new animal bedding and feed company that is visually grabbing and vibrant. We would like to see a website that displays trust, quality and confidence. Needs to be responsive and mobile friendly for all browsers and coded for both Android & IOS. SEO is also important.

Joomla or Wordpress – must be both desktop and mobile friendly with fast page load speed. Need the ability to edit ourselves in Wordpress or Joomla.

Full details attached below with some layout and content ideas.

Coding

Coded - Design and coding required

Number of Pages Required

5+ page

Font styles to use
Sans Serif

Requirements
Must have
• Needs to be responsive and mobile friendly for all browsers and coded for both Android & IOS. SEO is also important.

Wordpress – must be both desktop and mobile friendly with fast page load speed. Need the ability to edit ourselves in Wordpress.

Logo Colours:
Dark Brown
CMYK: 50 / 70 / 80 / 70
Pantone: 4625C

Orange
CMYK: 0 / 50 / 100 / 0
Pantone: 144C
Nice to have
• Use picture of building attached and super impose logo on building.

```html
<!DOCTYPE html>
<html lang="en">
<head>
<meta charset="utf-8">
<title>Golden Bale — Bedding &amp; Feed</title>
<link href="https://fonts.googleapis.com/css2?family=Bebas+Neue&family=Montserrat:wght@400;500;600;800&family=Open+Sans:wght@400;600&display=swap" rel="stylesheet">
<style>
:root{
  --orange:#f0902a;
  --brown:#4a2a14;
  --brown-deep:#3a2010;
  --text:#3b3b3b;
  --muted:#555;
  --light:#f5f5f7;
  --white:#fff;
}
*{margin:0;padding:0;box-sizing:border-box}
html,body{width:1200px;height:3604px;overflow:hidden;background:var(--white)}
body{position:relative;font-family:'Open Sans',sans-serif;color:var(--text)}
.abs{position:absolute}
.display{font-family:'Bebas Neue',sans-serif;font-weight:400}
.mont{font-family:'Montserrat',sans-serif}

/* header */
.contact-tab{left:630px;top:0;width:570px;height:39px;background:var(--brown);border-bottom-left-radius:38px 39px;display:flex;align-items:center;padding-left:50px;gap:18px;font-family:'Montserrat',sans-serif;font-size:14px;color:var(--white)}
.contact-tab .dot{width:24px;height:24px;border-radius:50%;background:var(--orange);display:inline-flex;align-items:center;justify-content:center;margin-right:9px;vertical-align:middle}
.contact-tab span{display:inline-flex;align-items:center;margin-right:14px}
.brand{left:161px;top:34px;display:flex;align-items:center;gap:14px}
.brand .mark{width:44px;height:44px;border-radius:50%;background:var(--orange)}
.brand .name{font-family:'Bebas Neue',sans-serif;font-size:44px;color:var(--brown);letter-spacing:3px;line-height:1}
.nav{top:71px;left:526px;display:flex;font-family:'Montserrat',sans-serif;font-size:14px;font-weight:500;color:var(--brown)}
.nav a{position:absolute;white-space:nowrap;text-decoration:none;color:inherit}
.nav a.active{color:var(--orange)}
.btn-quote{left:906px;top:60px;width:132px;height:38px;border-radius:19px;background:var(--orange);color:var(--white);font-family:'Montserrat',sans-serif;font-size:14px;font-weight:500;display:flex;align-items:center;justify-content:center;box-shadow:0 0 0 2px var(--white),0 0 0 3px var(--orange)}

/* hero */
.hero{left:0;top:119px;width:1200px;height:549px;background:linear-gradient(180deg,#3f5a23 0%,#5f7a2e 40%,#7d8a3a 62%,#6e6a2e 100%)}
.hero-title{left:0;top:556px;width:1200px;text-align:center;font-family:'Montserrat',sans-serif;font-weight:800;font-size:37px;color:var(--white);letter-spacing:-.5px}

/* about */
.about{left:0;top:668px;width:1200px;height:898px;background:var(--light)}
.hero-tab{left:540px;top:668px}
.about-heading{left:0;top:752px;width:1200px;display:flex;justify-content:center;align-items:center;gap:16px}
.about-heading .word{font-family:'Bebas Neue',sans-serif;font-size:46px;color:var(--orange)}
.about-heading .mark{width:40px;height:40px;border-radius:50%;background:var(--orange)}
.about-heading .name{font-family:'Bebas Neue',sans-serif;font-size:40px;color:var(--brown);letter-spacing:3px}
.about-lead{left:210px;top:828px;width:780px;text-align:center;font-size:15px;font-weight:600;line-height:24px;color:var(--brown-deep)}
.about-body{left:225px;top:915px;width:750px;text-align:center;font-size:15px;line-height:27px;color:var(--muted)}
.feature-circle{width:162px;height:162px;border-radius:50%;background:var(--white);box-shadow:0 4px 18px rgba(0,0,0,.06);display:flex;align-items:center;justify-content:center}
.feature-title{width:300px;text-align:center;font-family:'Bebas Neue',sans-serif;font-size:22px;color:var(--brown);letter-spacing:.5px}
.feature-text{width:300px;text-align:center;font-size:15px;line-height:24px;color:var(--muted)}

/* benefits */
.photo-round{border-radius:50%}
.photo-bedding{left:162px;top:1671px;width:417px;height:437px;background:radial-gradient(circle at 50% 40%,#8a5634 0%,#5a3520 45%,#9a8a4e 100%)}
.photo-feed{left:621px;top:2364px;width:417px;height:436px;background:radial-gradient(circle at 45% 40%,#c9834e 0%,#9a5a30 45%,#6a4a2a 100%)}
.sec-title{font-family:'Bebas Neue',sans-serif;font-size:44px;color:var(--brown);letter-spacing:.5px;line-height:1}
.sec-title .hl{color:var(--orange)}
.rule{height:3px;width:54px;background:var(--brown)}
.ticks{list-style:none;font-size:15px;color:var(--brown-deep)}
.ticks li{position:relative;padding-left:29px}
.ticks li svg{position:absolute;left:0;top:4px}
.btn-more{height:34px;border-radius:17px;background:var(--orange);color:var(--white);font-family:'Open Sans',sans-serif;font-size:14px;display:flex;align-items:center;justify-content:center;box-shadow:0 0 0 1px var(--white),0 0 0 2px var(--orange)}
.feed-intro{left:190px;top:2266px;width:820px;text-align:center;font-size:15px;line-height:24px;color:var(--muted)}

/* delivery */
.delivery{left:0;top:2885px;width:1200px;height:157px;border-top:1px solid #eee}
.flags{left:285px;top:2933px;width:179px;height:78px;background:linear-gradient(90deg,#2b4a9a 0%,#c8202a 45%,#e8e8e8 60%,#d8202a 100%);border-radius:4px}
.delivery-title{left:485px;top:2940px;font-family:'Bebas Neue',sans-serif;font-size:54px;color:var(--brown);letter-spacing:.5px}

/* newsletter */
.newsletter{left:0;top:3042px;width:1200px;height:270px;background:var(--light)}
.news-title{left:200px;top:3118px;width:240px;text-align:right;font-family:'Bebas Neue',sans-serif;font-size:44px;line-height:46px;color:var(--brown-deep)}
.news-divider{left:468px;top:3084px;width:2px;height:175px;background:#e2e2e4}
.news-note{left:514px;top:3135px;font-family:'Montserrat',sans-serif;font-size:12px;color:#777}
.news-field{left:506px;top:3162px;width:481px;height:40px;border-radius:20px;background:var(--white);border:1px solid #ddd;display:flex;align-items:center;padding-left:16px;font-family:'Montserrat',sans-serif;font-size:12px;color:#555}
.news-btn{right:3px;top:3px;position:absolute;width:118px;height:32px;border-radius:16px;background:var(--brown-deep);color:var(--white);font-family:'Montserrat',sans-serif;font-weight:800;font-size:15px;display:flex;align-items:center;justify-content:center}

/* footer */
.footer{left:0;top:3312px;width:1200px;height:292px;background:linear-gradient(180deg,#5a3420 0%,#4a2a18 55%,#3c2212 100%)}
.foot-brand{left:160px;top:3360px;width:260px;display:flex;flex-direction:column;align-items:center;gap:12px}
.foot-brand .mark{width:54px;height:54px;border-radius:50%;background:var(--white)}
.foot-brand .name{font-family:'Bebas Neue',sans-serif;font-size:46px;color:var(--white);letter-spacing:3px;line-height:1}
.foot-icon{width:60px;height:60px;border-radius:50%;background:var(--orange);display:flex;align-items:center;justify-content:center}
.foot-info{width:200px;text-align:center;font-family:'Montserrat',sans-serif;color:var(--white)}
.copyright{left:164px;top:3559px;font-family:'Montserrat',sans-serif;font-size:12px;color:var(--white)}
.copyright u{text-decoration:underline}
.social{width:22px;height:22px;border-radius:50%}
</style>
</head>
<body>

<!-- header -->
<div class="abs contact-tab">
  <span><i class="dot"><svg width="12" height="12" viewBox="0 0 24 24"><path d="M2 12L22 3l-5 18-6-6-5 3z" fill="#fff"/></svg></i>inquiry@goldenbale.com</span>
  <span><i class="dot"><svg width="12" height="12" viewBox="0 0 24 24"><path d="M6 2l4 4-2 3c1 3 4 6 7 7l3-2 4 4-3 4C10 22 2 14 2 5z" fill="#fff"/></svg></i>555 014 2290</span>
</div>
<div class="abs brand"><span class="mark"></span><span class="name">GOLDEN BALE</span></div>
<nav class="abs nav">
  <a class="active" style="left:0">Home</a>
  <a style="left:73px">About</a>
  <a style="left:144px">Feed</a>
  <a style="left:210px">Bedding</a>
  <a style="left:299px">Contact</a>
</nav>
<div class="abs btn-quote">Request Quote</div>

<!-- hero -->
<div class="abs hero" role="img" aria-label="Horses grazing in a green meadow in front of a line of trees"></div>
<div class="abs hero-title">WE ARE ANIMAL BEDDING AND FEED COMPANY</div>

<!-- about -->
<section class="abs about"></section>
<svg class="abs hero-tab" width="120" height="30" viewBox="0 0 120 30"><path d="M0 0h120c-22 0-32 28-60 28S22 0 0 0z" fill="#6e6a2e"/></svg>
<svg class="abs" style="left:589px;top:645px" width="22" height="30" viewBox="0 0 22 30"><rect x="1" y="1" width="20" height="28" rx="10" fill="none" stroke="#f0902a" stroke-width="2"/><path d="M7 12l4 4 4-4M7 17l4 4 4-4" stroke="#f0902a" stroke-width="1.6" fill="none"/></svg>

<div class="abs about-heading"><span class="word">ABOUT</span><span class="mark"></span><span class="name">GOLDEN BALE</span></div>
<p class="abs about-lead">Looking for the best bedding and feed for your horse, livestock or household pet look no further.&nbsp; We use premium locally sourced straw and hay in all of our products and are committed in providing quality products and service.</p>
<p class="abs about-body">Your animal deserves the very best in health and comfort to keep them healthy, strong and happy.&nbsp; Our products are designed for horses, livestock (goats, cattle and sheep), small caged animals (rabbits, guinea pigs and more). Golden Bale offers supply and delivery of fresh bedding as well as removal of waste bedding.&nbsp; Let us deliver you a container of fresh straw and haul your waste bedding away.&nbsp; A full service solution that is sustainable and responsible.</p>

<svg class="abs" style="left:0;top:1120px" width="1200" height="220" viewBox="0 0 1200 220"><path d="M0 115C80 165 180 180 230 180M390 130C430 100 480 80 520 70M680 70C730 90 780 115 815 140M970 175C1060 160 1140 110 1200 60" fill="none" stroke="#e6d8c4" stroke-width="1.5" stroke-dasharray="4 5"/></svg>

<div class="abs feature-circle" style="left:519px;top:1088px" role="img" aria-label="Icon of hands holding a gear"><svg width="70" height="70" viewBox="0 0 70 70"><circle cx="35" cy="24" r="12" fill="none" stroke="#f0902a" stroke-width="2.5"/><path d="M35 30V18M30 23l5-5 5 5" stroke="#f0902a" stroke-width="2.5" fill="none"/><path d="M8 40l10 20h10M62 40l-10 20H42" stroke="#4a2a14" stroke-width="2.5" fill="none"/></svg></div>
<div class="abs feature-title" style="left:450px;top:1270px">FULL SERVICE SOLUTION</div>
<div class="abs feature-text" style="left:450px;top:1301px">Dedicated in providing a full<br>service solution of bedding<br>supply &amp; waste removal</div>

<div class="abs feature-circle" style="left:227px;top:1192px" role="img" aria-label="Icon of a quality award badge"><svg width="64" height="70" viewBox="0 0 64 70"><circle cx="32" cy="28" r="20" fill="none" stroke="#4a2a14" stroke-width="2.5"/><circle cx="32" cy="28" r="11" fill="none" stroke="#f0902a" stroke-width="2.5"/><path d="M18 44l-8 18 10-3 4 8 6-15M46 44l8 18-10-3-4 8-6-15" stroke="#4a2a14" stroke-width="2.5" fill="none"/></svg></div>
<div class="abs feature-title" style="left:158px;top:1373px">QUALITY GUARANTEED</div>
<div class="abs feature-text" style="left:158px;top:1404px">Grown for quality - 100% natural<br>with no chemicals or additives</div>

<div class="abs feature-circle" style="left:811px;top:1192px" role="img" aria-label="Icon of a hand holding a coin"><svg width="70" height="66" viewBox="0 0 70 66"><circle cx="42" cy="18" r="13" fill="none" stroke="#f0902a" stroke-width="2.5"/><path d="M6 50l14-12h14l18-8 10 4-26 16H26" stroke="#4a2a14" stroke-width="2.5" fill="none"/></svg></div>
<div class="abs feature-title" style="left:742px;top:1373px">CONVENIENT &amp; COST EFFECTIVE</div>
<div class="abs feature-text" style="left:742px;top:1405px">Compressed bags , pellets or bulk<br>products saving in shipping costs</div>

<!-- bedding benefits -->
<div class="abs photo-round photo-bedding" role="img" aria-label="Two horses grazing on a paddock, shown in a round frame"></div>
<h2 class="abs sec-title" style="left:622px;top:1694px"><span class="hl">BEDDING</span> BENEFITS</h2>
<div class="abs rule" style="left:622px;top:1749px"></div>
<ul class="abs ticks" style="left:622px;top:1780px;width:340px;line-height:23px">
  <li style="margin-bottom:10px"><svg width="20" height="12" viewBox="0 0 20 12"><path d="M1 6l4 4 9-9M7 10l2 1 10-10" stroke="#f0902a" stroke-width="1.5" fill="none"/></svg>100% Natural Chopped Straw</li>
  <li style="margin-bottom:10px"><svg width="20" height="12" viewBox="0 0 20 12"><path d="M1 6l4 4 9-9M7 10l2 1 10-10" stroke="#f0902a" stroke-width="1.5" fill="none"/></svg>Low Dust</li>
  <li style="margin-bottom:10px"><svg width="20" height="12" viewBox="0 0 20 12"><path d="M1 6l4 4 9-9M7 10l2 1 10-10" stroke="#f0902a" stroke-width="1.5" fill="none"/></svg>Chemical &amp; Additive Free</li>
  <li style="margin-bottom:10px"><svg width="20" height="12" viewBox="0 0 20 12"><path d="M1 6l4 4 9-9M7 10l2 1 10-10" stroke="#f0902a" stroke-width="1.5" fill="none"/></svg>Clean &amp; Highly Absorbent</li>
  <li style="margin-bottom:10px"><svg width="20" height="12" viewBox="0 0 20 12"><path d="M1 6l4 4 9-9M7 10l2 1 10-10" stroke="#f0902a" stroke-width="1.5" fill="none"/></svg>Cheaper than Wood Shavings</li>
  <li style="margin-bottom:10px"><svg width="20" height="12" viewBox="0 0 20 12"><path d="M1 6l4 4 9-9M7 10l2 1 10-10" stroke="#f0902a" stroke-width="1.5" fill="none"/></svg>Economic – less used and less wasted</li>
  <li><svg width="20" height="12" viewBox="0 0 20 12"><path d="M1 6l4 4 9-9M7 10l2 1 10-10" stroke="#f0902a" stroke-width="1.5" fill="none"/></svg>Environmentally Friendly – Recyclable &amp;<br>Compostable</li>
</ul>
<div class="abs btn-more" style="left:622px;top:2049px;width:119px">KNOW MORE</div>

<!-- feed benefits -->
<h2 class="abs sec-title" style="left:0;top:2187px;width:1200px;text-align:center"><span class="hl">FEED</span> BENEFITS</h2>
<div class="abs rule" style="left:573px;top:2244px"></div>
<p class="abs feed-intro">Hay cubes and pellets are made from premium hay offering a variety of animals a feed that is non-GMO and packed with natural nutrients.&nbsp; These pellets and cubes are less bulky to handle, store and ship. As well, they reduce the amount of wasted feed.</p>
<ul class="abs ticks" style="left:162px;top:2402px;width:420px;line-height:23px">
  <li style="margin-bottom:12.2px"><svg width="20" height="12" viewBox="0 0 20 12"><path d="M1 6l4 4 9-9M7 10l2 1 10-10" stroke="#f0902a" stroke-width="1.5" fill="none"/></svg>100% Natural</li>
  <li style="margin-bottom:12.2px"><svg width="20" height="12" viewBox="0 0 20 12"><path d="M1 6l4 4 9-9M7 10l2 1 10-10" stroke="#f0902a" stroke-width="1.5" fill="none"/></svg>Chemical &amp; Additive Free</li>
  <li style="margin-bottom:12.2px"><svg width="20" height="12" viewBox="0 0 20 12"><path d="M1 6l4 4 9-9M7 10l2 1 10-10" stroke="#f0902a" stroke-width="1.5" fill="none"/></svg>Available in Pellets or Cubes</li>
  <li style="margin-bottom:12.2px"><svg width="20" height="12" viewBox="0 0 20 12"><path d="M1 6l4 4 9-9M7 10l2 1 10-10" stroke="#f0902a" stroke-width="1.5" fill="none"/></svg>High Protein Content</li>
  <li style="margin-bottom:12.2px"><svg width="20" height="12" viewBox="0 0 20 12"><path d="M1 6l4 4 9-9M7 10l2 1 10-10" stroke="#f0902a" stroke-width="1.5" fill="none"/></svg>Eliminate Waste In Feeding</li>
  <li style="margin-bottom:12.2px"><svg width="20" height="12" viewBox="0 0 20 12"><path d="M1 6l4 4 9-9M7 10l2 1 10-10" stroke="#f0902a" stroke-width="1.5" fill="none"/></svg>Clean - Eliminates Dust From Feeding Baled Hay</li>
  <li style="margin-bottom:12.2px"><svg width="20" height="12" viewBox="0 0 20 12"><path d="M1 6l4 4 9-9M7 10l2 1 10-10" stroke="#f0902a" stroke-width="1.5" fill="none"/></svg>Cost Effective</li>
  <li style="margin-bottom:12.2px"><svg width="20" height="12" viewBox="0 0 20 12"><path d="M1 6l4 4 9-9M7 10l2 1 10-10" stroke="#f0902a" stroke-width="1.5" fill="none"/></svg>Convenient</li>
  <li><svg width="20" height="12" viewBox="0 0 20 12"><path d="M1 6l4 4 9-9M7 10l2 1 10-10" stroke="#f0902a" stroke-width="1.5" fill="none"/></svg>Less wasted feed</li>
</ul>
<div class="abs btn-more" style="left:162px;top:2724px;width:119px">KNOW MORE</div>
<div class="abs photo-round photo-feed" role="img" aria-label="Foal and mare eating hay in a stable, shown in a round frame"></div>

<!-- delivery -->
<section class="abs delivery"></section>
<div class="abs flags" role="img" aria-label="Waving flags of the United States and Canada"></div>
<div class="abs delivery-title">DELIVERY IN USA &amp; CANADA</div>

<!-- newsletter -->
<section class="abs newsletter"></section>
<h2 class="abs news-title">NEWSLETTER<br>SIGN UP</h2>
<div class="abs news-divider"></div>
<div class="abs news-note">Subscribe to our newsletter to get the latest update to your inbox</div>
<div class="abs news-field">Enter your email address<span class="news-btn">SUBSCRIBE</span></div>

<!-- footer -->
<footer class="abs footer" role="img" aria-label="Aerial view of a ranch with barns, toned in dark brown"></footer>
<div class="abs foot-brand"><span class="mark"></span><span class="name">GOLDEN BALE</span></div>

<div class="abs foot-icon" style="left:520px;top:3376px"><svg width="22" height="28" viewBox="0 0 22 28"><path d="M11 1C5 1 1 5 1 11c0 7 10 16 10 16s10-9 10-16C21 5 17 1 11 1z" fill="#fff"/><circle cx="11" cy="11" r="4" fill="#f0902a"/></svg></div>
<div class="abs foot-info" style="left:450px;top:3459px;font-size:12px;line-height:16px">Delivery in Canada<br>&amp; USA</div>

<div class="abs foot-icon" style="left:714px;top:3370px"><svg width="24" height="24" viewBox="0 0 24 24"><path d="M6 2l4 4-2 3c1 3 4 6 7 7l3-2 4 4-3 4C10 22 2 14 2 5z" fill="#fff"/></svg></div>
<div class="abs foot-info" style="left:646px;top:3450px;font-size:13px">PHONE</div>
<div class="abs foot-info" style="left:646px;top:3469px;font-size:20px;font-weight:600">555 014 2290</div>

<div class="abs foot-icon" style="left:929px;top:3374px"><svg width="26" height="20" viewBox="0 0 26 20"><rect x="1" y="1" width="24" height="18" rx="2" fill="#fff"/><path d="M2 3l11 8 11-8" stroke="#f0902a" stroke-width="2" fill="none"/></svg></div>
<div class="abs foot-info" style="left:861px;top:3447px;font-size:13px">EMAIL</div>
<div class="abs foot-info" style="left:861px;top:3470px;font-size:14px;font-weight:500">info@goldenbale.com</div>

<div class="abs copyright">Copyright 2021 Golden Bale Animal Feed.All Rights Reserved | <u>SITE MAP</u></div>
<span class="abs social" style="left:918px;top:3555px;background:#3b5bab"></span>
<span class="abs social" style="left:951px;top:3555px;background:#2aa3e6"></span>
<span class="abs social" style="left:983px;top:3555px;background:#1a76b8"></span>
<span class="abs social" style="left:1016px;top:3555px;background:#6a7fa8"></span>

</body>
</html>
```